Label Design Refresh for existing High End Supplement line

Design a label for our high end supplement brand, packaged in a Cobal Blue bottle.... using Clear labels as the label stock media.

A clear label design will take advantage of the blue bottle and can incorporate any design element you create, metalic elements, new graphics etc.

our line spans 50 different product categories and over 400 unique SKUs, so any elements you suggest to differentiate products or categories will be appreciated.

see: www.quillantheralife.com
Updates

Need designers to meet project requirements. Full label, clear label stock design (clear background with exception for design elements and text etc.)

Target Market(s)

Men and Women 25-55 Health conscious and not price sensitive. Product is 5x higher cost than competition.

Industry/Entity Type

Sexual health for men and women. testosterone, hormone health, nootropics

Font styles to use
Sans Serif

Colors

Designer to choose colors to be used in the design.

Requirements
Must have
• Clear label design for Cobalt blue, packer style, pharma bottle. Must feature Velmora brand on front panel. Must show entire label panel design as 2.8in x 7.25in. Graphics can be full color with metalic or foil type elements.
Nice to have
• Name of products include: SHBG, Testosterone & Libido, Adrenal Support Phase 2, LH Formula, ADHD Phase1,
Should not have
• Busy designs that are stock images for supplement label layouts

```html
<!DOCTYPE html>
<html lang="en">
<head>
<meta charset="utf-8">
<title>Velmora Supplement Labels</title>
<link href="https://fonts.googleapis.com/css2?family=Barlow+Semi+Condensed:wght@400;500;700&family=Barlow+Condensed:wght@400;500&display=swap" rel="stylesheet">
<style>
  :root {
    --page: #ffffff;
    --cobalt: #1d2aa8;
    --cobalt-deep: #141c7a;
    --cobalt-shade: #0f1660;
    --silver: #e4e4ea;
    --gold: #d9c07a;
    --gold-soft: #c9a85a;
  }
  * { margin: 0; padding: 0; box-sizing: border-box; }
  html, body { width: 1200px; height: 1200px; overflow: hidden; background: var(--page); }
  .canvas { position: relative; width: 1200px; height: 1200px; }
  .label {
    position: absolute;
    top: 410px;
    width: 418px;
    height: 560px;
    border-radius: 18px;
    background: linear-gradient(180deg, var(--cobalt) 0%, var(--cobalt-deep) 70%, var(--cobalt-shade) 100%);
    color: var(--silver);
    font-family: "Barlow Semi Condensed", sans-serif;
  }
  .label--kidney { left: 152px; }
  .label--adrenal { left: 637px; }
  .brand {
    position: absolute; left: 42px; top: 28px;
    display: flex; align-items: center; gap: 8px;
    font-weight: 700; font-size: 40px; letter-spacing: -0.5px; color: var(--silver);
  }
  .brand-dot { width: 14px; height: 14px; border-radius: 50%; background: var(--gold); }
  .product-name {
    position: absolute; left: 40px; top: 130px;
    font-weight: 700; font-size: 76px; line-height: 1; letter-spacing: 1px;
  }
  .product-line {
    position: absolute; left: 42px; top: 220px;
    font-weight: 500; font-size: 27px; color: var(--gold); letter-spacing: 0.5px;
  }
  .benefits {
    position: absolute; left: 44px; top: 290px; width: 360px;
    list-style: none;
    font-family: "Barlow Condensed", sans-serif; font-size: 15px; line-height: 19.5px;
    text-transform: uppercase;
  }
  .benefits li { position: relative; padding-left: 14px; }
  .benefits li::before {
    content: ""; position: absolute; left: 0; top: 5px;
    width: 7px; height: 10px; border-radius: 6px 0 6px 0; background: var(--gold);
  }
  .count {
    position: absolute; left: 42px; top: 468px;
    display: flex; align-items: center; gap: 6px;
  }
  .count-number { font-weight: 700; font-size: 38px; line-height: 1; color: var(--gold); }
  .count-unit { font-family: "Barlow Condensed", sans-serif; font-size: 16px; line-height: 17px; text-transform: uppercase; }
  .supplement-type {
    position: absolute; left: 42px; top: 510px;
    font-family: "Barlow Condensed", sans-serif; font-size: 23px; letter-spacing: 0.5px;
  }
  .organ-art {
    position: absolute; top: 395px; width: 118px; height: 128px; border-radius: 14px;
    background: radial-gradient(circle, rgba(217,192,122,0.45) 0%, rgba(201,168,90,0.12) 75%);
  }
  .label--kidney .organ-art { left: 282px; }
  .label--adrenal .organ-art { left: 250px; top: 400px; width: 124px; height: 118px; }
</style>
</head>
<body>
<main class="canvas">

  <section class="label label--kidney">
    <div class="brand"><span class="brand-dot"></span>VELMORA</div>
    <h1 class="product-name">KIDNEY</h1>
    <p class="product-line">SUPPORT</p>
    <ul class="benefits">
      <li>Used for kidney disease, stones, and swelling</li>
      <li>Improve kidney function primarily by ridding the body of excess water and increasing urination</li>
      <li>The treatment of infectious cystitis and urethritis</li>
    </ul>
    <div class="count"><span class="count-number">60</span><span class="count-unit">Vegetable<br>Capsules</span></div>
    <p class="supplement-type">DIETARY SUPPLEMENT</p>
    <div class="organ-art" role="img" aria-label="Gold line illustration of a pair of kidneys"></div>
  </section>

  <section class="label label--adrenal">
    <div class="brand"><span class="brand-dot"></span>VELMORA</div>
    <h1 class="product-name">ADRENAL</h1>
    <p class="product-line">SUPPORT PHASE 2</p>
    <ul class="benefits">
      <li>Highest quality adaptogens</li>
      <li>Vitamin C and pantethine added</li>
      <li>Mix of herbal botanicals and mushrooms</li>
    </ul>
    <div class="count"><span class="count-number">60</span><span class="count-unit">Vegetable<br>Capsules</span></div>
    <p class="supplement-type">DIETARY SUPPLEMENT</p>
    <div class="organ-art" role="img" aria-label="Gold line illustration of a human brain"></div>
  </section>

</main>
</body>
</html>
```